Header/Logo Redesign

****WE HAVE FOUND THE DESIGNER WHO WILL BE HANDLING THIS PROJECT. PLEASE DONT SUBMIT ANY MORE DESIGNS.****
We have been working with a Web/Logo Designer on a new header and logo for our site. We like some of it, but other things need changing.
Overall Look: We are looking for something that is professional, yet still fresh. Most business two business websites seem old fashinoned. The site we like most is www.ledgerkite.com.
Header Thoughts:
-We like the color at the top of the header. The light purple on the menu bar is a little dull though. It seems to be grayed out too much. Notice the pop that www.ledgerkite.com has. We need that pop.
-The fonts on the menu bar don't pop either. I don't know if it is because the font is bad or the thickness of the font is bad or what.
-We are not sold on the green color in the logo and header. It is pretty good, but maybe we can test other colors?
Logo Thoughts:
-I am not sold on the green color. It is pretty good, but maybe test it out with some other colors?
-The logo does not pop like the www.ledgerkite.com logo pops.
-We had started thinking about doing an owl as part of our name/logo or maybe some other type of animal. Look at the ideas I had sent our original graphic designer.
A. http://markgrove.com/gallery/detail/113160 - i like that is simple, a little abstract, but I don't like that it is sort of evil.
B. http://markgrove.com/gallery/detail/61169 - i like that is abstract.
C. http://pixelbrine.files.hostplank.com/2012/05/tabrisk1.jpg - i like the slightly abstract.
D. http://snapquill.com/shots/353825-O-W-L - good - abrstract and slightly turned.
Target Market(s)
Sales and Marketing People - primarily a masculine audience in their 20s to 40s.
Industry/Entity Type
Business
Look and feel

```html
<!DOCTYPE html>
<html lang="en">
<head>
<meta charset="utf-8">
<title>Prospect207 Header</title>
<link rel="stylesheet" href="https://fonts.googleapis.com/css2?family=Arimo:wght@400;700&display=swap">
<style>
  :root {
    --header-top: #00213d;
    --header-bottom: #053a66;
    --nav-blue: #0a7ee2;
    --nav-blue-dark: #066ccb;
    --nav-active: #0b5fd0;
    --nav-active-light: #1a86ee;
    --panel-blue: #0a7ce0;
    --panel-deep: #0660b8;
    --tab-blue: #064d92;
    --field-navy: #053566;
    --field-text: #c3e2f7;
    --tab-text: #a9c9e6;
    --search-text: #2a6f8f;
    --page-grey: #efefef;
    --page-line: #e6e6e6;
    --white: #ffffff;
  }
  * { margin: 0; padding: 0; box-sizing: border-box; }
  html, body { width: 1200px; height: 400px; overflow: hidden; }
  body { font-family: "Arimo", Arial, sans-serif; }

  .canvas {
    position: relative;
    width: 1200px;
    height: 400px;
    background: repeating-linear-gradient(to bottom, var(--page-grey) 0 2px, var(--page-line) 2px 3px);
    overflow: hidden;
  }

  .masthead {
    position: absolute; left: 0; top: 0; width: 1200px; height: 68px;
    background: linear-gradient(to bottom, var(--header-top), var(--header-bottom));
  }
  .brand {
    position: absolute; left: 218px; top: 12px; height: 48px;
    display: flex; align-items: center; gap: 10px;
  }
  .brand-dot { width: 30px; height: 30px; border-radius: 50%; background: var(--white); }
  .brand-name { font-weight: 700; font-size: 42px; color: var(--white); letter-spacing: -1px; }

  .main-nav {
    position: absolute; left: 0; top: 68px; width: 1200px; height: 38px;
    background: linear-gradient(to bottom, var(--nav-blue), var(--nav-blue-dark));
    border-bottom: 1px solid #0a5fa8;
  }
  .nav-item {
    position: absolute; top: 0; height: 37px; line-height: 37px;
    font-weight: 700; font-size: 14.5px; color: var(--white);
    text-shadow: 0 1px 1px rgba(0,0,0,0.35);
  }
  .nav-item.is-active {
    left: 206px; width: 50px; text-align: center;
    background: linear-gradient(to bottom, var(--nav-active-light), var(--nav-active) 40%, var(--nav-active));
  }
  .nav-people { left: 294px; }
  .nav-companies { left: 385px; }
  .nav-downloads { left: 506px; }

  .search-field {
    position: absolute; left: 657px; top: 75px; width: 120px; height: 28px;
    background: var(--white); border-radius: 14px 0 0 14px;
    border: 1px solid #c9d9a8;
    padding-left: 158px;
    font-size: 12px; line-height: 26px; color: var(--search-text);
    padding: 0 0 0 15px;
  }

  .login-panel {
    position: absolute; left: 737px; top: 0; width: 247px; height: 135px;
    background: radial-gradient(ellipse at 50% 45%, var(--panel-blue) 55%, var(--panel-deep) 100%);
    border-radius: 0 0 4px 4px;
    box-shadow: 0 1px 2px rgba(0,0,0,0.25);
  }
  .signup-tab {
    position: absolute; right: 0; top: 0; width: 120px; height: 24px;
    background: var(--tab-blue); border-radius: 0 0 0 4px;
    font-weight: 700; font-size: 11px; line-height: 26px;
    text-align: center; color: var(--tab-text);
  }
  .login-field {
    position: absolute; left: 21px; width: 196px; height: 29px;
    background: var(--field-navy); border-radius: 4px;
    font-weight: 700; font-size: 11px; line-height: 29px;
    color: var(--field-text); padding-left: 24px;
  }
  .field-user { top: 45px; }
  .field-pass { top: 87px; padding-left: 27px; }
</style>
</head>
<body>
  <div class="canvas">
    <header class="masthead">
      <div class="brand">
        <span class="brand-dot"></span>
        <span class="brand-name">Prospect207</span>
      </div>
    </header>

    <nav class="main-nav">
      <span class="nav-item is-active">New</span>
      <span class="nav-item nav-people">People</span>
      <span class="nav-item nav-companies">Companies</span>
      <span class="nav-item nav-downloads">Downloads</span>
    </nav>

    <div class="search-field">search</div>

    <div class="login-panel">
      <div class="signup-tab">Free Sign Up</div>
      <div class="login-field field-user">user name</div>
      <div class="login-field field-pass">password</div>
    </div>
  </div>
</body>
</html>
```